Tallowbrook Mental Health Care for All

A4 flyer & A3 poster promoting a free service for everyone in the community with moderate to high risk of mental health difficulties. It’s a new service being introduced in a rural/remote community. We created two versions- could be front & back on the A4, & 2 different A3 posters. Perhaps a bi-fold with one side For Referrers & the other side For Patients?? We like the content of our drafts but they need to be presented professionally…. Yet, VERY patient friendly with easy to understand text, icons, etc… whatever is recommended. The indigenous artwork I’ve photographed is for background inspiration. It’s bush medicine. We would like to include something that communicates our respect for the traditional owners, elders past, present and emerging. Thank you.

Target Market(s)

Rural, remote people who are in distress and need access to mental health services

Industry/Entity Type

Mental health

Font styles to use
Other font styles liked:
• Calibri??

Colors
00AB8E
00BBA5
67D7C9
C6EFE9
E9F9F6

Requirements
Must have
• Free service; all welcome, call 52917703, we will support you
Nice to have
• Simple, easy to follow, communicates confidence and caring
Should not have
• Too much clutter. Too many words.

```html
<!DOCTYPE html>
<html lang="en">
<head>
<meta charset="utf-8">
<title>Fully Funded Mental Health Service – Clearwater Wellbeing</title>
<link href="https://fonts.googleapis.com/css2?family=Cinzel:wght@600;700;800&family=Poppins:wght@400;500;600;700&display=swap" rel="stylesheet">
<style>
  :root{
    --green-dark:#1b7a35;
    --green-deep:#176b2e;
    --green-light:#8cc63f;
    --ring:#d9efbf;
    --ink:#3b3b3b;
    --grey-head:#555555;
    --step-bg:#e7e0e1;
    --paper:#f8faf5;
    --white:#ffffff;
    --stage:#eef0ee;
  }
  *{box-sizing:border-box;margin:0;padding:0}
  html,body{width:794px;height:1200px;overflow:hidden;background:var(--stage)}
  body{font-family:"Poppins",Arial,sans-serif;color:var(--ink);position:relative}

  .sheet{position:absolute;top:341px;width:608px;height:862px;background:var(--paper);overflow:hidden;transform:scale(.6);transform-origin:0 0;box-shadow:0 4px 14px rgba(0,0,0,.18)}
  .sheet--service{left:22px}
  .sheet--coordination{left:407px;background:var(--white)}
  .abs{position:absolute}

  .brand{left:28px;top:26px;width:220px;text-align:center}
  .brand-mark{width:62px;height:62px;border:4px solid var(--green-dark);border-radius:50%;margin:0 auto 10px}
  .brand-name{font-family:"Cinzel",Georgia,serif;font-weight:700;color:var(--green-dark);font-size:21px;line-height:1.1}

  .cinzel{font-family:"Cinzel",Georgia,serif;font-weight:700}
  .title-kicker{left:32px;top:176px;color:var(--grey-head);font-size:29px;line-height:1}
  .title-main{left:32px;top:204px;color:var(--green-dark);font-size:52px;line-height:.96;font-weight:800}
  .title-sub{left:32px;top:308px;width:220px;display:flex;align-items:center;gap:8px;color:var(--grey-head);font-size:28px;line-height:1}
  .title-sub::before,.title-sub::after{content:"";flex:1;height:2px;background:var(--grey-head)}

  .photo{left:0;top:0}
  .heads-art{left:33px;top:355px;width:103px;height:92px;border-radius:48% 48% 40% 40%;background:linear-gradient(90deg,#d8a85c 0%,#c89a52 45%,#2f8a7a 55%,#1e6f66 100%)}

  .q-head{color:var(--green-dark);font-size:29px;line-height:1}
  .q-text{border-left:2px solid var(--ink);padding-left:9px;font-size:15.5px;line-height:1.18}

  .what-tab{left:233px;top:464px;width:135px;height:38px;background:var(--green-dark);border-radius:16px 16px 0 0;text-align:center;color:var(--white);font-size:24px;line-height:40px}
  .what-box{left:23px;top:515px;width:562px;height:142px;background:var(--green-dark);border-radius:12px;display:flex;padding:26px 6px 8px}
  .what-pill{left:143px;top:500px;width:322px;height:28px;background:var(--green-light);border-radius:10px;text-align:center;font-weight:700;color:var(--green-deep);font-size:17px;line-height:28px}
  .service{flex:1;display:flex;flex-direction:column;align-items:center;text-align:center;color:var(--white);font-size:12.5px;line-height:1.2;padding:0 8px}
  .service + .service{border-left:2px dashed rgba(255,255,255,.7)}
  .icon{width:44px;height:44px;border-radius:50%;background:var(--green-light);border:3px solid var(--ring);display:flex;align-items:center;justify-content:center;flex:none}
  .service .icon{margin-bottom:10px}
  .service p{min-height:60px;display:flex;align-items:center}

  .call-lead{font-weight:600;font-size:14px;line-height:1.2;text-transform:uppercase}
  .phone{height:36px;background:var(--green-light);border-radius:18px}
  .phone-icon{position:absolute;left:0;top:-3px;width:42px;height:42px;border-radius:50%;background:var(--green-dark);border:3px solid var(--white);display:flex;align-items:center;justify-content:center}
  .phone-number{position:absolute;left:60px;top:0;font-weight:700;color:var(--white);font-size:22px;line-height:36px;letter-spacing:1.5px}
  .call-note{font-size:14px;line-height:1.2}

  .footer{left:0;bottom:0;width:608px;height:56px}
  .footer-url{left:0;bottom:16px;width:608px;text-align:center;font-weight:600;color:var(--white);font-size:14px}

  /* coordination page */
  .co-title{left:32px;top:172px;font-size:30px;line-height:1;font-weight:800}
  .co-title .g{color:var(--green-dark)}
  .co-title .s{color:var(--grey-head)}
  .step{left:56px;width:239px;height:86px;background:var(--step-bg);padding:6px 8px 0 28px}
  .step h3{font-family:"Cinzel",Georgia,serif;font-weight:700;color:var(--green-dark);font-size:13.5px;line-height:1;margin-bottom:4px}
  .step li{list-style:none;position:relative;padding-left:9px;font-size:7.2px;line-height:1.3;margin-bottom:2px}
  .step li::before{content:"";position:absolute;left:0;top:3px;width:5px;height:5px;border-radius:50%;background:var(--green-light)}
  .step-num{left:32px;width:42px;height:42px;border-radius:50%;border:3px solid var(--white);color:var(--white);font-weight:700;font-size:18px;line-height:36px;text-align:center}
  .step-num--dark{background:var(--green-dark)}
  .step-num--light{background:var(--green-light)}
  .co-lead{left:338px;top:463px;font-weight:600;color:var(--grey-head);font-size:17px;line-height:1.25}
  .co-item{left:336px;width:260px;display:flex;align-items:center;gap:10px;font-size:11.5px;line-height:1.2}
</style>
</head>
<body>

<!-- Flyer: service overview -->
<main class="sheet sheet--service">
  <header class="brand abs">
    <div class="brand-mark"></div>
    <div class="brand-name">Clearwater Wellbeing</div>
  </header>

  <div class="title-kicker cinzel abs">Fully Funded</div>
  <h1 class="title-main cinzel abs">Mental<br>Health</h1>
  <div class="title-sub cinzel abs">Service</div>

  <svg class="photo abs" width="608" height="470" viewBox="0 0 608 470" role="img" aria-label="Photograph of a woman meditating cross-legged on grass under a clear sky, shown as a cross of tiles">
    <defs>
      <linearGradient id="sky-grass" x1="0" y1="0" x2="0" y2="1">
        <stop offset="0" stop-color="#b7d3ec"/>
        <stop offset=".45" stop-color="#dde8ef"/>
        <stop offset=".62" stop-color="#7fb8ad"/>
        <stop offset=".8" stop-color="#d9e3e0"/>
        <stop offset="1" stop-color="#86ad4a"/>
      </linearGradient>
    </defs>
    <g fill="url(#sky-grass)">
      <path d="M390 37a10 10 0 0 1 10-10h81a10 10 0 0 1 10 10v93H390z"/>
      <path d="M281 147a10 10 0 0 1 10-10h94v103H281z"/>
      <rect x="390" y="137" width="101" height="103"/>
      <path d="M496 137h92a10 10 0 0 1 10 10v93H496z"/>
      <path d="M281 244h104v101H291a10 10 0 0 1-10-10z"/>
      <rect x="390" y="244" width="101" height="101"/>
      <path d="M496 244h102v91a10 10 0 0 1-10 10H496z"/>
      <path d="M390 352h101v91a10 10 0 0 1-10 10h-81a10 10 0 0 1-10-10z"/>
    </g>
  </svg>

  <div class="heads-art abs" role="img" aria-label="Illustration of two head silhouettes in profile with brain line art"></div>

  <h2 class="q-head cinzel abs" style="left:155px;top:360px">Who?</h2>
  <p class="q-text abs" style="left:157px;top:398px">For people at risk of<br>moderate-severe<br>mental disorders</p>

  <div class="what-tab cinzel abs">What?</div>
  <section class="what-box abs">
    <div class="service">
      <div class="icon"><svg width="22" height="22" viewBox="0 0 28 28" fill="none" stroke="#fff" stroke-width="2" stroke-linecap="round" stroke-linejoin="round"><circle cx="14" cy="10" r="5"/><path d="M3 20c4-3 7-3 10-1l6 1c2 0 2 3 0 3h-6M3 24h14l7-4"/></svg></div>
      <p>Employ best practices in risk management + cognitive behavioural therapy</p>
    </div>
    <div class="service">
      <div class="icon"><svg width="22" height="22" viewBox="0 0 28 28" fill="none" stroke="#fff" stroke-width="2" stroke-linecap="round" stroke-linejoin="round"><circle cx="14" cy="14" r="10"/><path d="M9 14l4 4 7-8"/></svg></div>
      <p>Complement existing mental health services</p>
    </div>
    <div class="service">
      <div class="icon"><svg width="22" height="22" viewBox="0 0 28 28" fill="none" stroke="#fff" stroke-width="2" stroke-linecap="round" stroke-linejoin="round"><path d="M14 22s-8-5-8-11a4 4 0 0 1 8-1 4 4 0 0 1 8 1c0 6-8 11-8 11z"/><path d="M3 8v10l5 5M25 8v10l-5 5"/></svg></div>
      <p>Provide stepped care and needs based distribution of resources</p>
    </div>
  </section>
  <div class="what-pill abs">Co-ordinated care services</div>

  <p class="call-lead abs" style="left:33px;top:673px;width:240px">Please call our friendly reception staff on</p>
  <div class="phone abs" style="left:33px;top:717px;width:240px">
    <div class="phone-icon"><svg width="20" height="20" viewBox="0 0 24 24" fill="#fff"><path d="M6.6 10.8a15.1 15.1 0 0 0 6.6 6.6l2.2-2.2a1 1 0 0 1 1-.25 11.4 11.4 0 0 0 3.6.57 1 1 0 0 1 1 1V20a1 1 0 0 1-1 1A17 17 0 0 1 3 4a1 1 0 0 1 1-1h3.5a1 1 0 0 1 1 1 11.4 11.4 0 0 0 .57 3.6 1 1 0 0 1-.25 1z"/></svg></div>
    <span class="phone-number">5291 7703</span>
  </div>
  <p class="call-note abs" style="left:33px;top:765px;width:250px">to discuss any questions, queries or concerns.</p>

  <h2 class="q-head cinzel abs" style="left:322px;top:675px">How?</h2>
  <p class="q-text abs" style="left:324px;top:713px;width:258px;font-size:12.6px;line-height:1.25">Upon receiving your referral (Via GP, Self or Other), our reception staff will organise a brief interview to determine eligibility. Please allow 15 mins of time for this call.</p>

  <svg class="footer abs" viewBox="0 0 608 56" preserveAspectRatio="none">
    <path d="M0 28H150c8 0 10-2 13-11 3-9 6-11 17-11h248c11 0 14 2 17 11 3 9 5 11 13 11H608v28H0z" fill="#1b7a35"/>
  </svg>
  <div class="footer-url abs">www.clearwaterwellbeing.com.au</div>
</main>

<!-- Flyer: care co-ordination steps -->
<main class="sheet sheet--coordination">
  <header class="brand abs">
    <div class="brand-mark"></div>
    <div class="brand-name">Clearwater Wellbeing</div>
  </header>

  <h1 class="co-title cinzel abs"><span class="g">Tallowbrook P4<br>Clinical Mental</span><br><span class="s">Health Care<br>Co-ordination</span></h1>

  <svg class="photo abs" width="608" height="370" viewBox="0 0 608 370" role="img" aria-label="Photograph of a smiling family with a child and a cat outdoors in warm sunlight, shown as a cross of tiles">
    <defs>
      <linearGradient id="family-light" x1="0" y1="0" x2="1" y2="1">
        <stop offset="0" stop-color="#efe3c6"/>
        <stop offset=".45" stop-color="#d7a77a"/>
        <stop offset=".75" stop-color="#c9b59a"/>
        <stop offset="1" stop-color="#9fb15a"/>
      </linearGradient>
    </defs>
    <g fill="url(#family-light)">
      <path d="M416 23a10 10 0 0 1 10-10h72v77h-82z"/>
      <path d="M503 13h72a10 10 0 0 1 10 10v67h-82z"/>
      <path d="M330 107a10 10 0 0 1 10-10h70v83h-80z"/>
      <rect x="416" y="97" width="82" height="83"/>
      <rect x="503" y="97" width="82" height="83"/>
      <path d="M330 185h80v82h-70a10 10 0 0 1-10-10z"/>
      <rect x="416" y="185" width="82" height="82"/>
      <rect x="503" y="185" width="82" height="82"/>
      <path d="M503 273h82v72a10 10 0 0 1-10 10h-62a10 10 0 0 1-10-10z"/>
    </g>
  </svg>

  <section class="step abs" style="top:310px">
    <h3>Referral Triage</h3>
    <ul><li>Referral received via GP or Self or other</li><li>Eligibility determined through New Service Triage Form</li><li>Current GP referral required</li></ul>
  </section>
  <div class="step-num step-num--dark abs" style="top:332px">1</div>

  <section class="step abs" style="top:410px">
    <h3>Initial Consultation</h3>
    <ul><li>Understand consumer's health concerns and goals</li><li>Provide information on available services</li><li>Assess/manage safety risks</li><li>Facilitate access to appropriate support</li></ul>
  </section>
  <div class="step-num step-num--light abs" style="top:432px">2</div>

  <section class="step abs" style="top:510px">
    <h3>Case Conference</h3>
    <ul><li>Multidisciplinary case conference with health professionals</li><li>Coordinate patient care plan</li><li>Ensure access to necessary services</li></ul>
  </section>
  <div class="step-num step-num--dark abs" style="top:532px">3</div>

  <section class="step abs" style="top:610px">
    <h3>Case Management</h3>
    <ul><li>CW Health Professionals assist with care plan implementation</li><li>Direct mental health services for complex cases</li></ul>
  </section>
  <div class="step-num step-num--light abs" style="top:632px">4</div>

  <section class="step abs" style="top:707px">
    <h3>Case Review and<br>Evaluation</h3>
    <ul><li>Measure and report on outcomes, patient safety, satisfaction</li><li>Plan transition from P4 service</li></ul>
  </section>
  <div class="step-num step-num--dark abs" style="top:729px">5</div>

  <h2 class="q-head cinzel abs" style="left:332px;top:320px">Who?</h2>
  <p class="q-text abs" style="left:340px;top:357px;font-size:14.5px">For consumers with<br>Moderate-Severe risk of<br>mental disorder</p>

  <h2 class="q-head cinzel abs" style="left:336px;top:428px">What?</h2>
  <p class="co-lead abs">Co-ordinated care<br>services that :</p>

  <div class="co-item abs" style="top:523px">
    <div class="icon"><svg width="22" height="22" viewBox="0 0 28 28" fill="none" stroke="#fff" stroke-width="2" stroke-linecap="round" stroke-linejoin="round"><circle cx="14" cy="10" r="5"/><path d="M3 20c4-3 7-3 10-1l6 1c2 0 2 3 0 3h-6M3 24h14l7-4"/></svg></div>
    <p>Employ best practices in risk management + cognitive behavioural therapy</p>
  </div>
  <div class="co-item abs" style="top:581px">
    <div class="icon"><svg width="22" height="22" viewBox="0 0 28 28" fill="none" stroke="#fff" stroke-width="2" stroke-linecap="round" stroke-linejoin="round"><circle cx="14" cy="14" r="10"/><path d="M9 14l4 4 7-8"/></svg></div>
    <p>Complement existing mental health services</p>
  </div>
  <div class="co-item abs" style="top:643px">
    <div class="icon"><svg width="22" height="22" viewBox="0 0 28 28" fill="none" stroke="#fff" stroke-width="2" stroke-linecap="round" stroke-linejoin="round"><path d="M14 22s-8-5-8-11a4 4 0 0 1 8-1 4 4 0 0 1 8 1c0 6-8 11-8 11z"/><path d="M3 8v10l5 5M25 8v10l-5 5"/></svg></div>
    <p>Provide stepped care and needs based distribution of resources</p>
  </div>

  <p class="call-lead abs" style="left:338px;top:695px;width:240px;font-size:12.5px">Please call our friendly reception staff on</p>
  <div class="phone abs" style="left:340px;top:735px;width:190px;height:30px">
    <div class="phone-icon" style="width:34px;height:34px;top:-2px"><svg width="16" height="16" viewBox="0 0 24 24" fill="#fff"><path d="M6.6 10.8a15.1 15.1 0 0 0 6.6 6.6l2.2-2.2a1 1 0 0 1 1-.25 11.4 11.4 0 0 0 3.6.57 1 1 0 0 1 1 1V20a1 1 0 0 1-1 1A17 17 0 0 1 3 4a1 1 0 0 1 1-1h3.5a1 1 0 0 1 1 1 11.4 11.4 0 0 0 .57 3.6 1 1 0 0 1-.25 1z"/></svg></div>
    <span class="phone-number" style="left:48px;font-size:18px;line-height:30px">5291 7703</span>
  </div>
  <p class="call-note abs" style="left:338px;top:773px;width:220px;font-size:11px">to discuss any questions, queries or concerns.</p>

  <svg class="footer abs" viewBox="0 0 608 56" preserveAspectRatio="none">
    <path d="M0 28H142c8 0 10-2 13-11 3-9 6-11 17-11h248c11 0 14 2 17 11 3 9 5 11 13 11H608v28H0z" fill="#1b7a35"/>
  </svg>
  <div class="footer-url abs" style="left:-8px">www.clearwaterwellbeing.com.au</div>
</main>

</body>
</html>
```